Art Deco Wedding Invitation

We need a wedding invitation designed for a 1920's Art Deco theme.
The wedding will take place in Berlin, which had a glamorous, modern and wild culture in the 1920's. This may offer some design inspiration.
The couple's names are Rowan and Liesel and the wedding will take place on May 8, 2015.

Industry/Entity Type

Wedding

```html
<!DOCTYPE html>
<html lang="en">
<head>
<meta charset="utf-8">
<title>Liesel &amp; Rowan – Wedding Stationery Suite</title>
<link href="https://fonts.googleapis.com/css2?family=Alfa+Slab+One&family=Josefin+Sans:wght@400;600&display=swap" rel="stylesheet">
<style>
:root{
  --page:#ffffff;
  --cream:#fbf3ec;
  --frame:#c7ccd1;
  --frame-light:#e1e4e7;
  --ink:#7f93ab;
  --ink-dark:#5f7591;
  --slate:#a9bbc5;
  --petal:#c8343c;
  --caption:#6d6d6d;
}
*{margin:0;padding:0;box-sizing:border-box}
html,body{width:1200px;height:765px;overflow:hidden;background:var(--page)}
.sheet{position:relative;width:1200px;height:765px;font-family:"Josefin Sans",sans-serif;color:var(--ink)}
.piece{position:absolute;background:var(--cream);border:1px solid var(--frame);
  box-shadow:inset 0 0 0 4px var(--frame-light),inset 0 0 0 5px var(--frame);
  display:flex;flex-direction:column;align-items:center;justify-content:center;text-align:center;padding:9px;overflow:hidden}
.piece.bold-frame{box-shadow:inset 0 0 0 4px var(--frame),inset 0 0 0 6px var(--ink)}
.pattern-floral{position:absolute;background:linear-gradient(135deg,#f4f1ef,#d9e0e6 55%,#e9dcdc);border:1px solid var(--frame)}
.pattern-dense{position:absolute;background:linear-gradient(135deg,#b7c4ce,#9fb1be 60%,#b6a9b0);border:1px solid var(--frame)}
.pattern-stripe{position:absolute;background:linear-gradient(90deg,#dde2e6,#cfd6dc);border:1px solid var(--frame)}
.display{font-family:"Alfa Slab One",serif;color:var(--ink);letter-spacing:.5px;line-height:1}
.small{font-size:4px;letter-spacing:.4px;text-transform:uppercase;line-height:1.5;color:var(--ink)}
.label{font-size:5px;font-weight:600;letter-spacing:.5px;text-transform:uppercase;color:var(--ink-dark)}
.mono{display:flex;align-items:center;justify-content:center;border-radius:50%;background:var(--slate);color:var(--cream);font-family:"Alfa Slab One",serif}
.mono.light{background:var(--cream);color:var(--ink);border:1px solid var(--slate)}
.pill{width:12px;height:5px;border-radius:3px;background:var(--slate)}
.rule{width:80%;height:1px;background:var(--frame);margin:3px 0}
.caption{position:absolute;font-size:4px;line-height:1.5;letter-spacing:.3px;text-transform:uppercase;color:var(--caption)}
.caption b{font-weight:600;color:#444}
.menu-cols{display:flex;width:100%;justify-content:space-around;margin-top:4px}
.menu-cols div{display:flex;flex-direction:column;align-items:center;gap:2px;width:25%;border-left:1px solid var(--frame)}
.menu-cols div:first-child{border-left:0}
.icon{width:7px;height:7px;border:1px solid var(--ink);border-radius:50%}
.band{position:absolute;left:888px;width:239px;height:32px;border:1px solid var(--frame);display:flex;align-items:center;justify-content:center}
.band.plain{background:var(--cream)}
.band.solid{background:var(--slate)}
.band .line{position:absolute;left:10px;right:10px;top:50%;height:1px;background:var(--frame)}
.sticker{position:absolute;width:38px;height:38px;border:1px solid var(--frame);background:var(--cream);display:flex;align-items:center;justify-content:center}
</style>
</head>
<body>
<main class="sheet">

<!-- Wedding invitation -->
<div class="pattern-floral" style="left:55px;top:88px;width:158px;height:114px" role="img" aria-label="Blue vine pattern with red blossoms on cream"></div>
<div class="mono" style="position:absolute;left:121px;top:131px;width:26px;height:26px;font-size:8px">L&amp;R</div>
<div class="pattern-dense" style="left:232px;top:88px;width:158px;height:114px" role="img" aria-label="Dense slate-blue vine pattern with red blossoms"></div>
<div class="mono light" style="position:absolute;left:298px;top:131px;width:26px;height:26px;font-size:8px">L&amp;R</div>

<section class="piece" style="left:45px;top:218px;width:160px;height:114px;padding:12px 14px">
  <div style="display:flex;width:100%;justify-content:space-between;align-items:center">
    <span class="small" style="text-align:left;width:32px">Together with their families</span>
    <span class="display" style="font-size:15px;text-align:left;flex:1;margin-left:4px">LIESEL<br>&amp;ROWAN</span>
  </div>
  <div class="rule" style="width:100%;margin:4px 0"></div>
  <div style="display:flex;width:100%;justify-content:space-between;align-items:center">
    <div style="text-align:left"><div class="label">Friday · May</div><div class="display" style="font-size:14px">08</div></div>
    <div class="label">The Marlow<br>Garden Hotel<br><span class="small">Central Berlin</span></div>
    <div><div class="small">In the year</div><div class="display" style="font-size:11px">2015</div></div>
  </div>
</section>
<div class="caption" style="left:45px;top:342px"><b>Wedding invitation (front)</b><br>A7 = 5 x 7<br>A7 = 7 x 5<br>Square = 5.25 x 5.25</div>

<section class="piece" style="left:232px;top:218px;width:158px;height:114px">
  <div class="mono" style="width:18px;height:18px;font-size:6px">L&amp;R</div>
</section>
<div class="caption" style="left:232px;top:342px"><b>Wedding invitation (back)</b><br>A7 = 5 x 7<br>A7 = 7 x 5<br>Square = 5.25 x 5.25</div>

<section class="piece" style="left:404px;top:218px;width:158px;height:114px;padding:11px">
  <div style="width:100%;height:100%;background:var(--slate);display:flex;align-items:center;justify-content:center">
    <div class="mono light" style="width:18px;height:18px;font-size:6px">L&amp;R</div>
  </div>
</section>
<div class="caption" style="left:480px;top:342px"><b>Wedding invitation (b&amp;w pattern)</b><br>A7 = 5 x 7<br>A7 = 7 x 5<br>Square = 5.25 x 5.25</div>

<!-- Program / menu cards -->
<section class="piece" style="left:738px;top:10px;width:114px;height:158px;padding:0">
  <div class="pattern-floral" style="inset:0" role="img" aria-label="Blue vine border with red blossoms"></div>
  <div style="position:absolute;inset:8px;background:var(--cream);border:1px solid var(--frame);display:flex;flex-direction:column;align-items:center;justify-content:center;gap:3px">
    <div class="display" style="font-size:9px">DINNER<br>MENU</div>
    <div class="label">May eighth, 2015</div>
    <div class="label">First course</div><div class="small">Chilled pea soup, mint</div>
    <div class="label">Second course</div><div class="small">Seared trout, dill butter</div>
    <div class="label">Entrée</div><div class="small">Roast lamb, spring greens</div>
    <div class="label">Dessert</div><div class="small">Lemon tart, cream</div>
    <div class="pill"></div>
    <div class="small">Coffee and petits fours</div>
  </div>
</section>

<section class="piece" style="left:738px;top:180px;width:114px;height:158px;gap:3px">
  <div class="display" style="font-size:7px">DINNER MENU MAY<br>EIGHTH, 2015</div>
  <div class="label">First course</div><div class="small">Chilled pea soup, mint</div>
  <div class="label">Second course</div><div class="small">Seared trout, dill butter</div>
  <div class="label">Entrée</div><div class="small">Roast lamb, spring greens</div>
  <div class="label">Dessert</div><div class="small">Lemon tart, cream</div>
  <div class="pill"></div>
  <div class="small">Coffee and petits fours</div>
</section>
<div class="caption" style="left:738px;top:344px"><b>Program card<br>Menu card</b><br>A7 = 5 x 7</div>

<section class="piece" style="left:866px;top:38px;width:158px;height:112px">
  <div class="display" style="font-size:9px">DINNER MENU</div>
  <div class="rule"></div>
  <div class="menu-cols">
    <div><span class="icon"></span><span class="label">First course</span><span class="small">Pea soup</span></div>
    <div><span class="icon"></span><span class="label">Second course</span><span class="small">Seared trout</span></div>
    <div><span class="icon"></span><span class="label">Entrée</span><span class="small">Roast lamb</span></div>
    <div><span class="icon" style="border-radius:0"></span><span class="label">Dessert</span><span class="small">Lemon tart</span></div>
  </div>
  <div class="small" style="margin-top:6px">8 May 2015</div>
</section>
<section class="piece" style="left:1032px;top:38px;width:158px;height:112px">
  <div class="display" style="font-size:9px">DINNER MENU</div>
  <div class="rule"></div>
  <div class="menu-cols">
    <div><span class="icon"></span><span class="label">First course</span><span class="small">Pea soup</span></div>
    <div><span class="icon"></span><span class="label">Second course</span><span class="small">Seared trout</span></div>
    <div><span class="icon"></span><span class="label">Entrée</span><span class="small">Roast lamb</span></div>
    <div><span class="icon"></span><span class="label">Dessert</span><span class="small">Lemon tart</span></div>
  </div>
  <div class="small" style="margin-top:6px">8 May 2015</div>
</section>

<!-- Belly bands -->
<div class="band pattern-floral" style="top:182px" role="img" aria-label="Belly band in blue vine pattern"></div>
<div class="band plain" style="top:220px"><span class="line"></span><span class="mono" style="position:relative;width:18px;height:18px;font-size:5px">L&amp;R</span></div>
<div class="band solid" style="top:258px"><span class="line" style="background:#c3d0d7"></span><span class="mono light" style="position:relative;width:18px;height:18px;font-size:5px">L&amp;R</span></div>
<div class="caption" style="left:888px;top:294px"><b>Belly band (solid)</b><br>10.5 x 1.25</div>
<div class="band pattern-floral" style="top:308px" role="img" aria-label="Belly band in blue vine pattern with red blossoms"></div>
<div class="band pattern-stripe" style="top:346px;height:30px" role="img" aria-label="Belly band in fine grey stripe pattern"></div>
<div class="caption" style="left:888px;top:428px"><b>Belly band (pattern)</b><br>10.5 x 1.25</div>

<!-- Thank you & accommodations -->
<section class="piece" style="left:97px;top:403px;width:126px;height:97px">
  <div class="display" style="font-size:11px">THANK YOU</div>
  <div class="pill" style="margin-top:4px"></div>
  <div class="mono" style="position:absolute;right:12px;bottom:12px;width:16px;height:16px;font-size:5px">L&amp;R</div>
</section>
<div class="caption" style="left:97px;top:506px"><b>Thank you card</b><br>4.25 x 5.5</div>

<section class="piece" style="left:256px;top:414px;width:115px;height:82px;gap:2px">
  <div class="display" style="font-size:8px">Accomodations</div>
  <div class="label">Halvard House Hotel</div><div class="small">Kestrelweg 7, Berlin</div>
  <div class="label">Linnet Court Hotel</div><div class="small">Amselgasse 2, Berlin</div>
  <div class="mono" style="position:absolute;right:10px;bottom:10px;width:13px;height:13px;font-size:4px">L&amp;R</div>
</section>
<div class="caption" style="left:256px;top:502px"><b>Accomodation card</b><br>3.50 x 5</div>

<section class="piece" style="left:384px;top:389px;width:114px;height:79px;gap:2px">
  <div class="display" style="font-size:7px">Accomodations</div>
  <div class="label">Halvard House Hotel</div><div class="small">Kestrelweg 7, Berlin</div>
  <div class="label">Linnet Court Hotel</div><div class="small">Amselgasse 2, Berlin</div>
</section>
<section class="piece bold-frame" style="left:384px;top:477px;width:114px;height:81px;gap:2px">
  <div class="display" style="font-size:7px">Accomodations</div>
  <div class="label">Halvard House Hotel</div><div class="small">Kestrelweg 7, Berlin</div>
  <div class="label">Linnet Court Hotel</div><div class="small">Amselgasse 2, Berlin</div>
  <div class="mono" style="position:absolute;right:10px;bottom:10px;width:12px;height:12px;font-size:3px">L&amp;R</div>
</section>

<!-- Schedule, reception, RSVP -->
<section class="piece bold-frame" style="left:8px;top:535px;width:115px;height:80px">
  <div class="display" style="font-size:7px">SCHEDULE<br>OF EVENTS</div>
  <div class="menu-cols">
    <div><span class="icon"></span><span class="small">Vows</span><span class="small">4:00 PM</span></div>
    <div><span class="icon"></span><span class="small">Cocktails</span><span class="small">5:00 PM</span></div>
    <div><span class="icon"></span><span class="small">Dinner</span><span class="small">7:00 PM</span></div>
    <div><span class="icon"></span><span class="small">Party</span><span class="small">10:00 PM</span></div>
  </div>
  <div class="small" style="margin-top:4px">More details on our wedding website</div>
</section>

<section class="piece" style="left:130px;top:535px;width:114px;height:80px;gap:3px">
  <div class="small">Please join us for a</div>
  <div class="display" style="font-size:8px">Reception<br>Dinner</div>
  <div class="small">Immediately following the ceremony</div>
</section>
<div class="caption" style="left:130px;top:628px"><b>Reception card</b><br>3.50 x 5</div>

<section class="piece" style="left:258px;top:535px;width:114px;height:80px;gap:2px">
  <div class="display" style="font-size:9px">RSVP</div>
  <div class="small" style="width:80%">The favor of a reply is requested by the first of April</div>
  <div class="label" style="align-self:flex-start;margin-left:12px">M ____________</div>
  <div class="small" style="align-self:flex-start;margin-left:12px;text-align:left">___ Accepts with pleasure<br>___ Declines with regret</div>
</section>
<div class="caption" style="left:258px;top:628px"><b>RSVP</b><br>4.5l</div>

<!-- Place cards & directions -->
<div class="pattern-floral" style="left:43px;top:659px;width:92px;height:39px" role="img" aria-label="Blue vine pattern with red blossoms"></div>
<section class="piece" style="left:43px;top:698px;width:92px;height:37px;box-shadow:none;align-items:flex-start;padding-left:8px">
  <div class="mono" style="width:16px;height:16px;font-size:5px">L&amp;R</div>
</section>
<section class="piece" style="left:142px;top:659px;width:93px;height:76px;padding:0;justify-content:flex-end;box-shadow:none">
  <div style="position:absolute;left:0;right:0;top:0;height:38px;background:var(--slate)"></div>
  <div class="mono" style="position:absolute;top:11px;width:14px;height:14px;font-size:4px;background:var(--ink)">L&amp;R</div>
  <div class="display" style="font-size:6px;margin-bottom:13px">LIESEL <span class="small">and</span> ROWAN</div>
</section>
<div class="caption" style="left:43px;top:741px"><b>Place card</b><br>3.5 x 4</div>

<section class="piece" style="left:264px;top:655px;width:116px;height:80px">
  <svg style="position:absolute;inset:0" width="116" height="80" viewBox="0 0 116 80" aria-hidden="true">
    <path d="M6 30 L60 6 M30 74 L110 20 M14 60 L50 74" stroke="#dfe3e7" stroke-width="7" fill="none"/>
  </svg>
  <div class="display" style="font-size:11px;position:relative">DIRECTIONS</div>
  <div class="small" style="position:relative;margin-top:3px">For more information</div>
</section>
<div class="caption" style="left:264px;top:741px"><b>I card</b></div>

<!-- Bridal shower -->
<section class="piece" style="left:405px;top:567px;width:114px;height:158px;gap:3px">
  <div class="small">Please join us for a</div>
  <div class="pill"></div>
  <div class="display" style="font-size:11px">BRIDAL<br>SHOWER</div>
  <div class="small">Honoring</div>
  <div class="display" style="font-size:11px">LIESEL</div>
  <div class="mono" style="width:11px;height:11px;font-size:3px;margin-top:6px">L&amp;R</div>
  <div class="small">The Marlow Garden Hotel<br>25th April</div>
</section>
<div class="caption" style="left:405px;top:731px"><b>Bridal shower</b><br>A7 = 5 x 7<br>A7 = 7 x 5<br>Square = 5.25 x 5.25</div>

<!-- Envelope pattern & save the date -->
<div class="pattern-floral" style="left:558px;top:463px;width:160px;height:115px" role="img" aria-label="Envelope liner in blue vine pattern with red blossoms"></div>
<div class="caption" style="left:562px;top:588px"><b>Envelope pattern</b></div>

<section class="piece" style="left:557px;top:610px;width:120px;height:115px;gap:2px">
  <div class="display" style="font-size:10px">Save the<br>Date</div>
  <div class="display" style="font-size:6px">LIESEL &amp; ROWAN</div>
  <div class="label">Are getting married</div>
  <div class="small">May 8, 2015 · Berlin</div>
  <div class="pill"></div>
  <div class="small">Invitation to follow</div>
</section>
<div class="caption" style="left:557px;top:731px"><b>Save the date</b><br>A7 = 5 x 7<br>A7 = 7 x 5<br>Square = 5.25 x 5.25</div>

<!-- Greeting / folded card -->
<section class="piece" style="left:738px;top:393px;width:115px;height:187px;padding:0;box-shadow:none">
  <div style="position:absolute;left:0;right:0;top:0;height:82px;background:var(--slate);display:flex;align-items:center;justify-content:center">
    <div class="mono" style="width:16px;height:16px;font-size:5px;background:var(--ink)">L&amp;R</div>
  </div>
  <div style="position:absolute;left:4px;right:4px;top:86px;bottom:4px;border:1px solid var(--frame);display:flex;flex-direction:column;align-items:center;justify-content:center;gap:2px">
    <div class="small">For the bride &amp; groom</div>
    <div class="display" style="font-size:7px">LIESEL &amp; ROWAN</div>
  </div>
</section>
<div class="caption" style="left:740px;top:584px"><b>Greeting cards</b><br>A7 = 5 x 7<br>Square = 5.25 x 5.25</div>
<div class="caption" style="left:740px;top:602px"><b>Table number</b><br>5.25 x 5.25</div>

<!-- Table number -->
<section class="piece" style="left:738px;top:618px;width:115px;height:120px;gap:1px">
  <div class="display" style="font-size:10px">TABLE</div>
  <div class="display" style="font-size:28px">26</div>
  <div class="mono" style="width:14px;height:14px;font-size:4px;margin-top:3px">L&amp;R</div>
</section>
<div class="caption" style="left:738px;top:744px"><b>Table number</b><br>5.25 x 5.25</div>

<!-- Stickers -->
<div class="sticker" style="left:890px;top:474px"><div class="mono light" style="width:30px;height:30px;font-size:8px">L&amp;R</div></div>
<div class="sticker" style="left:934px;top:474px;background:var(--ink)"><div class="mono light" style="width:30px;height:30px;font-size:3px;line-height:1.3">LIESEL<br>&amp;<br>ROWAN</div></div>
<div class="sticker" style="left:978px;top:474px"><div class="mono" style="width:30px;height:30px;font-size:7px">L&amp;R</div></div>
<div class="sticker pattern-floral" style="left:1021px;top:474px" role="img" aria-label="Square sticker in blue vine pattern"></div>
<div class="caption" style="left:890px;top:516px"><b>Stickers<br>Monograms</b><br>1.5"</div>
<div class="mono" style="position:absolute;left:932px;top:542px;width:37px;height:37px;font-size:8px;box-shadow:0 0 0 2px #e1e4e7">L&amp;R</div>
<div class="pattern-stripe" style="left:974px;top:542px;width:36px;height:36px;border-radius:50%" role="img" aria-label="Round sticker in fine grey stripe pattern"></div>
<div class="caption" style="left:890px;top:584px"><b>Stickers<br>Monograms (pattern)</b><br>1.5"</div>

<!-- Envelope wrap labels -->
<div class="pattern-floral" style="left:890px;top:660px;width:168px;height:17px" role="img" aria-label="Envelope wrap label in blue vine pattern"></div>
<div class="pattern-dense" style="left:890px;top:686px;width:168px;height:17px" role="img" aria-label="Envelope wrap label in slate vine pattern"></div>
<div class="caption" style="left:890px;top:708px"><b>Envelope wrap<br>Adress labels</b><br>7.25 x 10.75</div>

</main>
</body>
</html>
```